Buchcover-Design für Ratgeber & Arbeitsbuch
Zielgruppe
Ratgeber und Arbeitsbuch, einfach geschrieben für Menschen, die mit Geld nicht gut umgehen können. Titel: Oje, das Konto ist schon leer. Soll Einsparpotenziale und Möglichkeiten der einfachen Geldanlage für jedermann darstellen. Liefert als Arbeitsbuch Checklisten und Tabellenblätter zum selbst ausfüllen.
Aufgabenstellung
Format A4 hoch, Zielgruppe junge Leute, die wenig Erfahrung im Umgang mit Geld haben. bei denen das Geld nie reicht und die bei der Selbstkontrolle Schwierigkeiten haben.

```html
<!DOCTYPE html>
<html lang="de">
<head>
<meta charset="utf-8">
<title>Oje, das Konto ist schon leer – Buchcover</title>
<link rel="stylesheet" href="https://fonts.googleapis.com/css2?family=Anton&family=League+Spartan:wght@700&family=Crimson+Text&display=swap">
<style>
  :root {
    --stage: #4d4d4d;
    --paper: #ffffff;
    --ink: #000000;
    --title-grey: #474747;
    --shirt: #111111;
    --denim: #5a7aa8;
  }
  * { margin: 0; padding: 0; box-sizing: border-box; }
  html, body { width: 1200px; height: 1200px; overflow: hidden; background: var(--stage); }
  .canvas { position: relative; width: 1200px; height: 1200px; background: var(--stage); }
  .cover {
    position: absolute; left: 231px; top: 77px; width: 738px; height: 1045px;
    background: var(--paper); border: 3px solid var(--ink);
  }
  .title-main {
    position: absolute; left: 74px; top: 61px; width: 580px; height: 220px;
    display: flex; justify-content: space-between;
    font-family: "Anton", sans-serif; font-size: 220px; line-height: 1;
    color: var(--title-grey);
    text-shadow: -8px 2px 0 var(--ink);
  }
  .title-letter { display: inline-block; transform: scaleX(1.4); transform-origin: center top; }
  .title-comma { position: absolute; left: 0; top: 0; width: 732px; height: 300px; }
  .title-sub {
    position: absolute; left: 0; right: 0; top: 292px;
    text-align: center;
    font-family: "League Spartan", sans-serif; font-weight: 700;
    font-size: 45px; line-height: 1; color: var(--ink); letter-spacing: -0.5px;
  }
  .author {
    position: absolute; left: 0; right: 0; top: 355px;
    text-align: center; font-family: "Crimson Text", serif; font-size: 22px; color: var(--ink);
  }
  .tagline {
    position: absolute; left: 0; right: 0; top: 392px;
    text-align: center; font-family: "Crimson Text", serif; font-size: 30px; color: var(--ink);
  }
  .photo {
    position: absolute; left: 105px; top: 463px; width: 505px; height: 418px;
  }
  .blurb {
    position: absolute; left: 0; right: 0; top: 917px;
    text-align: center; font-family: "Crimson Text", serif; font-size: 25px; line-height: 35px; color: var(--ink);
  }
</style>
</head>
<body>
<div class="canvas">
  <div class="cover">
    <h1 class="title-main" aria-label="Oje,">
      <span class="title-letter">O</span><span class="title-letter">J</span><span class="title-letter">E</span>
    </h1>
    <svg class="title-comma" viewBox="0 0 732 300" aria-hidden="true">
      <polygon points="670,224 705,228 710,253 685,294 667,280 678,265 664,254 664,231" fill="var(--ink)"/>
      <polygon points="676,221 711,225 716,250 691,291 673,277 684,262 670,251 670,228" fill="var(--title-grey)"/>
    </svg>
    <div class="title-sub">DAS KONTO IST SCHON LEER!</div>
    <div class="author">Dr. Bernhard Solm, Hamburg</div>
    <div class="tagline">Der Weg aus Deiner Finanznot</div>
    <svg class="photo" viewBox="0 0 505 418" role="img" aria-label="Foto: junger Mann in schwarzem T-Shirt und Jeansshorts zieht seine leeren Hosentaschen heraus">
      <defs>
        <linearGradient id="photoTone" x1="0" y1="0" x2="0" y2="1">
          <stop offset="0" stop-color="var(--shirt)"/>
          <stop offset="0.36" stop-color="var(--shirt)"/>
          <stop offset="0.42" stop-color="var(--denim)"/>
          <stop offset="1" stop-color="var(--denim)"/>
        </linearGradient>
      </defs>
      <rect x="0" y="0" width="505" height="418" fill="url(#photoTone)" opacity="0.85"/>
    </svg>
    <div class="blurb">
      Ein Ratgeber und Arbeitsbuch für Leute,<br>
      die, trotz regelmäßigen Einkommens,<br>
      immer zu wenig Geld haben.
    </div>
  </div>
</div>
</body>
</html>
```